Square graphic for social media post

I want to create a 1080 x 1080px all-black image for the quote below that I can share on social media. I want the emphasis to be primarily on the quote, secondarily on the portrait, and third (smallest) on the logo. I want the background on the portrait to be edited so it's transparent and just shows the face of the person on a black background (no brick wall visible).

Graphic color: black
Text color: white
Content: "What we went through is going to make the greatest generation of hoteliers our industry has ever seen." << biggest text
Dorian Welk << smaller text
President, Marrowgate Hotels << smaller text
[image of person - use whichever version looks better to you]
[Add Lodging Ledger logo - whichever looks better to you]

This image needs to be readable when sized down much smaller (400x400?) so want the text and portrait to take up most of the space.

I'd like the output both as PNG and original file (preferably Canva). Thanks!

Target Market(s)

Hotel managers

Industry/Entity Type

Hospitality

Font styles to use
Sans Serif

Colors

Designer to choose colors to be used in the design.

Requirements
Must have
• Needs to focus on the quote and the person quoted (the portrait)

```html
<!DOCTYPE html>
<html lang="en">
<head>
<meta charset="utf-8">
<title>Quote Card – Dorian Welk</title>
<link href="https://fonts.googleapis.com/css2?family=Open+Sans:ital,wght@1,300;1,400;1,700;1,800&display=swap" rel="stylesheet">
<style>
  :root {
    --bg: #000000;
    --text: #ffffff;
    --text-soft: #e6e6e6;
    --portrait-light: #4a4a4a;
    --portrait-mid: #333333;
    --portrait-dark: #1e1e1e;
    --portrait-shade: #141414;
  }
  html, body {
    margin: 0;
    padding: 0;
    width: 1200px;
    height: 1200px;
    overflow: hidden;
    background: var(--bg);
  }
  .quote-card {
    position: relative;
    width: 1200px;
    height: 1200px;
    background: var(--bg);
    overflow: hidden;
    font-family: "Open Sans", Arial, sans-serif;
    color: var(--text);
  }
  .portrait {
    position: absolute;
    inset: 0;
    background:
      radial-gradient(ellipse 270px 360px at 570px 470px, var(--portrait-light) 0%, var(--portrait-mid) 60%, rgba(51,51,51,0) 100%),
      radial-gradient(ellipse 360px 330px at 560px 260px, var(--portrait-dark) 0%, var(--portrait-dark) 70%, rgba(30,30,30,0) 100%),
      radial-gradient(ellipse 700px 380px at 600px 1200px, var(--portrait-dark) 0%, var(--portrait-shade) 70%, rgba(20,20,20,0) 100%),
      radial-gradient(ellipse 200px 260px at 600px 1080px, var(--portrait-mid) 0%, rgba(51,51,51,0) 100%);
  }
  .brand-mark {
    position: absolute;
    left: 100px;
    top: 92px;
    width: 40px;
    height: 40px;
    border-radius: 50%;
    background: var(--text);
  }
  .publisher {
    position: absolute;
    left: 900px;
    top: 98px;
    width: 270px;
    text-align: center;
    font-size: 20px;
    line-height: 26px;
    font-weight: 700;
    font-style: italic;
    letter-spacing: 4px;
    text-transform: uppercase;
    color: var(--text);
  }
  .quote {
    position: absolute;
    left: 98px;
    top: 598px;
    margin: 0;
    font-size: 58px;
    line-height: 83px;
    font-weight: 800;
    font-style: italic;
    text-transform: uppercase;
    white-space: nowrap;
    color: var(--text);
  }
  .attribution {
    position: absolute;
    left: 98px;
    top: 1006px;
  }
  .attribution-name {
    margin: 0;
    font-size: 36px;
    line-height: 46px;
    font-weight: 800;
    font-style: italic;
    text-transform: uppercase;
  }
  .attribution-role {
    margin: 8px 0 0;
    font-size: 25px;
    line-height: 32px;
    font-weight: 300;
    font-style: italic;
    text-transform: uppercase;
    color: var(--text-soft);
  }
</style>
</head>
<body>
  <main class="quote-card">
    <div class="portrait" role="img" aria-label="Darkened portrait of Dorian Welk, smiling, in an open-collar shirt and dark jacket on a black background"></div>

    <div class="brand-mark" aria-hidden="true"></div>
    <div class="publisher">Lodging Ledger</div>

    <blockquote class="quote">"What we went through is<br>going to make the greatest<br>generation of hoteliers our<br>industry has ever seen."</blockquote>

    <div class="attribution">
      <p class="attribution-name">Dorian Welk</p>
      <p class="attribution-role">President, Marrowgate Hotels</p>
    </div>
  </main>
</body>
</html>
```